Chic, award winning Billboard wanted

Our restaurant is a modern and chic restaurant with AWESOME service, Fresh seafood and aged steaks in Costa Rica (where great service is a rarity as well as refined cooking).
The restaurant is called K Seafood & Grill, located in Manuel Antonio, Costa Rica
Our current marketing line is "K is not just dinner, it's a whole evening" Our colours are Pantone u498 blue and black as background
Go to our web site to see our style www.Kseafoodgrillrica.com
We have secured a 3.5 metre high by 9 metre wide billboard on the main highway and looking for an outstanding design to drive traffic to our business.
People associate Seafood too much with our restaurant, so we want to have our logo very present, but have the words "seafood"; "grill"; "aged steaks"; "lounge" kind of floating around the Z so that people don't associate our restaurant with only one type of food.
REMEMBER THIS BILLBOARD IS ON A MAIN HIGHWAY THAT PEOPLE ARE TRAVELLING AT 55 MILES PER HOUR!
check out our voyageranks for customer reviews: http://www.voyageranks.com/Eatery_Review-g551832-d7730194-Reviews-K_Seafood_Grill-Manuel_Antonio_National_Park_Province_of_Puntarenas.html
Target Market(s)
Travelling American & European Tourists to National Park,
Other font styles liked:
- Century Gothic
Requirements
Must have
- Want a fun and interesting billboard that engages people, not a static information "Logo, name, phone number"
- Needs to have phone number: 2615-3082
- Needs to have Voyageranks logo
Nice to have
- See attached ad done for a local magazine for the "look"

```html
<!DOCTYPE html>
<html lang="en">
<head>
<meta charset="utf-8">
<title>K Seafood &amp; Grill — Billboard</title>
<link rel="stylesheet" href="https://fonts.googleapis.com/css2?family=Questrial&family=Lato:wght@700;900&display=swap">
<style>
  :root {
    --page: #ffffff;
    --frame: #e3e3e3;
    --night: #000000;
    --glow: #0b0a7a;
    --brand-blue: #0a8fd6;
    --ink-light: #ffffff;
    --logo-box: #1a1a1a;
    --logo-edge: #6d6d6d;
    --ring: #d9d9df;
    --badge: #ffffff;
  }
  * { box-sizing: border-box; margin: 0; padding: 0; }
  html, body { width: 1200px; height: 1001px; overflow: hidden; background: var(--page); }
  .canvas {
    position: relative; width: 1200px; height: 1001px;
    border: 3px solid var(--frame); background: var(--page);
  }
  .billboard {
    position: absolute; left: 34px; top: 283px; width: 1138px; height: 440px;
    background:
      radial-gradient(ellipse 520px 330px at 760px 200px, var(--glow) 0%, rgba(11,10,122,0.55) 45%, rgba(0,0,0,0) 100%),
      var(--night);
    overflow: hidden;
  }
  .brand-mark {
    position: absolute; left: 42px; top: 58px; width: 148px; height: 146px;
    background: var(--logo-box); border: 1px solid var(--logo-edge);
    display: flex; align-items: center; justify-content: center; text-align: center;
    font-family: "Questrial", sans-serif; color: var(--brand-blue);
    font-size: 21px; line-height: 1.25; padding: 10px;
  }
  .tagline-lead {
    position: absolute; left: 206px; top: 165px;
    font-family: "Questrial", sans-serif; font-size: 42px; color: var(--ink-light);
    white-space: nowrap;
  }
  .tagline-punch {
    position: absolute; left: 44px; top: 238px;
    font-family: "Lato", sans-serif; font-weight: 900; font-size: 52px; color: var(--brand-blue);
    white-space: nowrap; letter-spacing: 0.3px;
  }
  .review-badge {
    position: absolute; left: 58px; top: 389px; width: 166px; height: 30px;
    background: var(--badge); border-radius: 2px;
  }
  .call-line {
    position: absolute; left: 268px; top: 378px;
    font-family: "Lato", sans-serif; font-weight: 700; font-size: 35px; color: var(--ink-light);
    white-space: nowrap;
  }
  .dish-wheel { position: absolute; left: 640px; top: 0; width: 498px; height: 440px; }
</style>
</head>
<body>
<div class="canvas">
  <section class="billboard">
    <div class="brand-mark">K Seafood &amp; Grill</div>
    <p class="tagline-lead">is Not Just Dinner,</p>
    <p class="tagline-punch">It’s a Whole Evening.</p>
    <div class="review-badge" role="img" aria-label="Voyageranks review badge"></div>
    <p class="call-line">Call Us on 2615-3082</p>

    <svg class="dish-wheel" viewBox="0 0 498 440" aria-hidden="false">
      <defs>
        <radialGradient id="pasta" cx="50%" cy="50%" r="50%">
          <stop offset="0" stop-color="#e8c98a"/><stop offset="1" stop-color="#f3efe6"/>
        </radialGradient>
        <radialGradient id="lounge" cx="50%" cy="50%" r="50%">
          <stop offset="0" stop-color="#8a5a34"/><stop offset="1" stop-color="#c79a62"/>
        </radialGradient>
        <radialGradient id="fish" cx="50%" cy="50%" r="50%">
          <stop offset="0" stop-color="#7a5a3c"/><stop offset="1" stop-color="#4a4a4a"/>
        </radialGradient>
        <radialGradient id="steak" cx="50%" cy="50%" r="50%">
          <stop offset="0" stop-color="#7d5a45"/><stop offset="1" stop-color="#e9e4dc"/>
        </radialGradient>
        <radialGradient id="ribs" cx="50%" cy="50%" r="50%">
          <stop offset="0" stop-color="#5a2a1c"/><stop offset="1" stop-color="#f2efe9"/>
        </radialGradient>
      </defs>
      <circle cx="282" cy="225" r="160" fill="none" stroke="var(--ring)" stroke-width="9"/>
      <g stroke="#ffffff" stroke-width="6">
        <circle cx="131" cy="155" r="79" fill="url(#pasta)" role="img" aria-label="Photo of seafood pasta with shrimp"/>
        <circle cx="299" cy="90" r="72" fill="url(#lounge)" role="img" aria-label="Photo of lounge seating with orange cushions"/>
        <circle cx="438" cy="205" r="80" fill="url(#fish)" role="img" aria-label="Photo of whole grilled fish with prawns"/>
        <circle cx="354" cy="348" r="78" fill="url(#steak)" role="img" aria-label="Photo of grilled aged steak with vegetables"/>
        <circle cx="160" cy="346" r="80" fill="url(#ribs)" role="img" aria-label="Photo of glazed ribs with vegetables"/>
      </g>
    </svg>
  </section>
</div>
</body>
</html>
```